Web Design Project for an IT product called "TELVOS"

Hello!

We need a web design for a new IT product called "TELVOS". The product consists of 2 software applications, one is on an Android based tablet, the other on a windows 7 computer. The system is used in the production for conducting time studies (e.g. everything that has to do with time measuring in the production). The design should include the company logo ("DRUF"), and the logo of the methodology used ("KOLU" - see www.kolu-example.de), the rest is up to you! We already made a concept for the app logo, but it can be tweaked in any way...
Updates

Will upload a document with exact description!

Updated the files... Made some screenshots of the app on the Android device & Windows 7

Reason: Will make a poll & let you know the decision tomorrow!

Target Market(s)

Larger production companies middle management, technology departments

Industry/Entity Type

Computer

Requirements
Must have
• - company logo "DRUF" - included
- methodology logo "KOLU" (see www.kolu-example.de) - included
Nice to have
• - our logo of the app tweaked and somehow integrated

```html
<!DOCTYPE html>
<html lang="fr">
<head>
<meta charset="utf-8">
<title>TELVOS – DRUF</title>
<link href="https://fonts.googleapis.com/css2?family=Ubuntu:ital,wght@0,300;0,400;0,500;1,400;1,500&display=swap" rel="stylesheet">
<style>
  :root {
    --page-bg: #e9eaee;
    --hero-light: #fbfbfc;
    --ink: #2b2b2b;
    --muted: #6f6f6f;
    --heading-blue: #1f5a7a;
    --link-blue: #1a8fd6;
    --nav-top: #555555;
    --nav-bottom: #252525;
    --nav-divider: #5c5c5c;
    --orange-top: #ffa533;
    --orange-bottom: #f07c00;
    --accent-orange: #e8791a;
    --footer-bg: #d9dde6;
    --line: #d6d8de;
    --shot-frame: #c9ccd2;
  }
  * { box-sizing: border-box; margin: 0; padding: 0; }
  html, body { width: 1200px; height: 1038px; overflow: hidden; }
  body {
    font-family: "Ubuntu", sans-serif;
    color: var(--ink);
    background: var(--page-bg);
    position: relative;
  }

  /* Header */
  .site-header {
    position: absolute; left: 0; top: 0; width: 1200px; height: 122px;
    background: linear-gradient(90deg, #f1f2f4, #fdfdfd 50%, #eceef1);
  }
  .brand {
    position: absolute; left: 86px; top: 28px; width: 187px; height: 68px;
    display: flex; align-items: center; justify-content: center;
    border: 2px solid #111;
    font-size: 40px; font-weight: 500; letter-spacing: 2px; color: #111;
  }
  .contact-block {
    position: absolute; right: 82px; top: 10px; text-align: right;
  }
  .contact-label { font-size: 13px; color: var(--muted); letter-spacing: .5px; }
  .contact-phone { font-size: 17px; color: #333; margin-top: 3px; }
  .contact-mail { font-size: 17px; font-style: italic; color: var(--link-blue); text-decoration: underline; display: block; margin-top: 1px; }
  .search {
    position: absolute; left: 930px; top: 79px; width: 196px; height: 27px;
    border-radius: 14px; background: #e3e4e7;
    box-shadow: inset 0 1px 3px rgba(0,0,0,.18);
    font-size: 11.5px; font-style: italic; color: #a3a3a3;
    padding: 7px 0 0 14px;
  }
  .search svg { position: absolute; right: 10px; top: 6px; }

  /* Navigation */
  .main-nav {
    position: absolute; left: 0; top: 122px; width: 1200px; height: 45px;
    background: linear-gradient(var(--nav-top), #3a3a3a 50%, var(--nav-bottom));
  }
  .main-nav ul { list-style: none; display: flex; position: absolute; left: 88px; top: 0; height: 45px; }
  .main-nav li {
    height: 45px; display: flex; align-items: center; justify-content: center;
    color: #fff; font-size: 16px;
    border-left: 1px solid var(--nav-divider);
  }
  .main-nav li:last-child { border-right: 1px solid var(--nav-divider); }

  /* Hero */
  .hero {
    position: absolute; left: 0; top: 167px; width: 1200px; height: 483px;
    background: radial-gradient(ellipse 700px 400px at 300px 80px, var(--hero-light), #eceef2 75%);
    border-bottom: 2px solid var(--line);
  }
  .hero-title {
    position: absolute; left: 86px; top: 56px; width: 400px;
    font-size: 27px; font-weight: 400; line-height: 34px; color: var(--heading-blue);
  }
  .hero-lead {
    position: absolute; left: 86px; top: 127px; width: 470px;
    font-size: 14.5px; font-weight: 500; font-style: italic; line-height: 19px; color: #444;
  }
  .hero-text {
    position: absolute; left: 86px; top: 172px; width: 470px;
    font-size: 14px; line-height: 19px; color: var(--muted);
  }
  .hero-text p + p { margin-top: 19px; }
  .cta {
    position: absolute; left: 86px; top: 341px; width: 180px; height: 50px;
    border-radius: 9px;
    background: linear-gradient(var(--orange-top), var(--orange-bottom));
    box-shadow: 0 2px 3px rgba(0,0,0,.2);
    color: #fff; font-size: 24px; display: flex; align-items: center; justify-content: center;
  }
  .app-shot {
    position: absolute; left: 613px; top: 42px; width: 513px; height: 361px;
    border: 4px solid var(--shot-frame); border-radius: 8px;
    background: linear-gradient(#e4e8ef 0 12%, #f4f5f7 12%);
    box-shadow: 0 2px 6px rgba(0,0,0,.25);
  }

  /* Specialization */
  .section-title {
    position: absolute; left: 86px; top: 680px;
    font-size: 26px; font-weight: 400; color: #3a3a3a; letter-spacing: .3px;
  }
  .feature { position: absolute; top: 749px; width: 228px; }
  .feature-icon { position: absolute; left: 0; top: 0; width: 42px; height: 44px; border-radius: 6px; }
  .feature-title {
    margin-left: 53px; font-size: 19px; font-weight: 400; line-height: 23px; color: var(--heading-blue);
  }
  .feature-text {
    margin-top: 11px; font-size: 12.5px; line-height: 19px; color: #333;
    text-align: justify; hyphens: auto; -webkit-hyphens: auto;
  }
  .read-more {
    position: absolute; top: 154px; left: 0;
    font-size: 12.5px; color: var(--accent-orange); text-decoration: underline;
  }

  /* Footer */
  .site-footer {
    position: absolute; left: 0; top: 954px; width: 1200px; height: 84px;
    background: var(--footer-bg); border-top: 1px solid #c9ced8;
  }
  .footer-links { position: absolute; left: 86px; top: 24px; font-size: 12px; color: var(--muted); }
  .footer-links span.sep { margin: 0 5px; }
  .copyright { position: absolute; left: 86px; top: 45px; font-size: 12px; color: var(--muted); }
  .method-name {
    position: absolute; left: 918px; top: 30px; font-size: 26px; font-weight: 500; color: #7f8a95; letter-spacing: 1px;
  }
  .method-badge {
    position: absolute; left: 1058px; top: 14px; width: 54px; height: 54px; border-radius: 50%;
    background: #c4c9d2;
  }
</style>
</head>
<body>
  <header class="site-header">
    <div class="brand">DRUF</div>
    <div class="contact-block">
      <div class="contact-label">Contact</div>
      <div class="contact-phone">(102) 555 0147</div>
      <a class="contact-mail">info@druf-example.com</a>
    </div>
    <div class="search">Enter your search...
      <svg width="16" height="16" viewBox="0 0 16 16"><circle cx="6.5" cy="6.5" r="5" fill="none" stroke="#8a8a8a" stroke-width="2"/><line x1="10" y1="10" x2="15" y2="15" stroke="#8a8a8a" stroke-width="2.2"/></svg>
    </div>
  </header>

  <nav class="main-nav">
    <ul>
      <li style="width:128px">Description</li>
      <li style="width:125px">Technology</li>
      <li style="width:184px">Supported devices</li>
      <li style="width:114px">Support</li>
      <li style="width:169px">Download manual</li>
      <li style="width:148px">Download demo</li>
      <li style="width:96px">Contact</li>
      <li style="width:74px">FAQ</li>
    </ul>
  </nav>

  <section class="hero">
    <h1 class="hero-title">Le Lorem Ipsum est simplement du faux texte.</h1>
    <p class="hero-lead">Contrairement à une opinion répandue, le Lorem Ipsum n'est pas simplement du texte aléatoire.</p>
    <div class="hero-text">
      <p>Plusieurs variations de Lorem Ipsum peuvent être trouvées ici ou là, mais la majeure partie d'entre elles a été altérée par l'addition d'humour ou de mots aléatoires qui ne ressemblent.</p>
      <p>pas une seconde à du texte standard. Si vous voulez utiliser un passage du Lorem Ipsum, vous devez être sûr qu'il n'y a rien d'embarrassant caché dans le texte. Tous les générateurs de Lorem Ipsum sur Internet tendent à reproduire.</p>
    </div>
    <a class="cta">Get it now</a>
    <div class="app-shot" role="img" aria-label="Screenshot of the TELVOS desktop application with a project tree and a time measurement chart"></div>
  </section>

  <h2 class="section-title">Software specialization</h2>

  <article class="feature" style="left:86px">
    <div class="feature-icon" role="img" aria-label="Stacked cubes icon" style="background:linear-gradient(135deg,#4aa3d8,#e0522c)"></div>
    <h3 class="feature-title">Heading<br>One</h3>
    <p class="feature-text">Le Lorem Ipsum est simplement du faux texte employé dans la composition et la mise en page avant impression.</p>
    <a class="read-more">Read More</a>
  </article>
  <article class="feature" style="left:356px">
    <div class="feature-icon" role="img" aria-label="Clock and calendar icon" style="background:linear-gradient(135deg,#7fb6e0,#4f9a3c)"></div>
    <h3 class="feature-title">Heading<br>Two</h3>
    <p class="feature-text">Le Lorem Ipsum est simplement du faux texte employé dans la composition et la mise en page avant impression.</p>
    <a class="read-more">Read More</a>
  </article>
  <article class="feature" style="left:627px">
    <div class="feature-icon" role="img" aria-label="Pie chart icon" style="background:linear-gradient(135deg,#8ed13a,#2a7fc4)"></div>
    <h3 class="feature-title">Heading<br>Three</h3>
    <p class="feature-text">Le Lorem Ipsum est simplement du faux texte employé dans la composition et la mise en page avant impression.</p>
    <a class="read-more">Read More</a>
  </article>
  <article class="feature" style="left:896px">
    <div class="feature-icon" role="img" aria-label="Clipboard with check mark icon" style="background:linear-gradient(135deg,#b7c3cf,#3aa34a)"></div>
    <h3 class="feature-title">Heading<br>Four</h3>
    <p class="feature-text">Le Lorem Ipsum est simplement du faux texte employé dans la composition et la mise en page avant impression.</p>
    <a class="read-more">Read More</a>
  </article>

  <footer class="site-footer">
    <div class="footer-links">Description<span class="sep">|</span>Technology<span class="sep">|</span>Supported devices<span class="sep">|</span>Support<span class="sep">|</span>Download manual<span class="sep">|</span>Download demo<span class="sep">|</span>Contact<span class="sep">|</span>FAQ</div>
    <div class="copyright">© Copyrights 2012 All rights Reserved</div>
    <div class="method-name">KOLU</div>
    <div class="method-badge" role="img" aria-label="Supported platform badge"></div>
  </footer>
</body>
</html>
```